Business Card Design Project

New Business Card design for Travorel Technology Ltd using new Logo and new Tagline for staffing company.

About us from our website - www.travorel-example.net:

TraVorel is a leading and recognized Electronic Entertainment, Workforce Augmentation, and Project Management solutions provider with clients in Electronic Entertainment, Legal, Technology, Government and other verticals that range in size from start up organizations to Zentora 300 companies. TraVorel is certified as an 8(a) minority and woman owned enterprise, established in 1998.

Target Market(s)

Companies in Electronic Entertainment, Legal, Government and Technology

Industry/Entity Type

Business

Requirements
Must have
• Must include in small letters the following information on back:

Established in 1998
8(a)(w)(e), Cage #7KQW4, DUNS #412306957

Front should have the following:
Dale Merrow
Vice President
5870 Brookhollow Court
Lindenvale, QX 908172
555-318-2046 X 100
555-742-9813 Fax
555-318-2046 Toll Free
name@travorel-example.net

Our Tagline: Connect • Collaborate • Achieve

```html
<!DOCTYPE html>
<html lang="en">
<head>
<meta charset="utf-8">
<title>TraVorel Business Cards</title>
<link rel="stylesheet" href="https://fonts.googleapis.com/css2?family=Arimo:wght@400;700&display=swap">
<style>
  :root {
    --brand-blue: #0a55a3;
    --ink-grey: #58585a;
    --paper: #ffffff;
    --backdrop: #e4e4e4;
    --text-font: "Arimo", Arial, sans-serif;
  }
  * { margin: 0; padding: 0; box-sizing: border-box; }
  html, body { width: 1200px; height: 900px; overflow: hidden; }
  body { background: var(--backdrop); font-family: var(--text-font); position: relative; }

  .card {
    position: absolute;
    width: 515px;
    height: 315px;
    background: var(--paper);
    box-shadow: 0 3px 10px rgba(0,0,0,0.25);
    overflow: hidden;
  }
  .card--front { left: 485px; top: 135px; }
  .card--back  { left: 205px; top: 465px; }

  .wordmark {
    position: absolute;
    color: var(--ink-grey);
    font-weight: 700;
    letter-spacing: -0.5px;
    white-space: nowrap;
  }
  .card--front .wordmark { left: 55px; top: 60px; font-size: 34px; }
  .card--back .wordmark { left: 0; right: 0; top: 98px; text-align: center; font-size: 48px; }

  .tagline {
    position: absolute;
    left: 40px;
    top: 168px;
    width: 180px;
    text-align: center;
    color: var(--brand-blue);
    font-weight: 700;
    font-size: 15px;
    line-height: 22px;
  }

  .name-band {
    position: absolute;
    left: 302px;
    top: 68px;
    right: 0;
    height: 70px;
    background: var(--brand-blue);
    color: #fff;
    padding: 14px 0 0 20px;
  }
  .name-band .person-name { font-size: 18px; font-weight: 700; letter-spacing: 0.3px; }
  .name-band .person-title { font-size: 14px; margin-top: 2px; }

  .contact-list {
    position: absolute;
    left: 298px;
    top: 157px;
    list-style: none;
    color: var(--ink-grey);
    font-size: 14px;
    line-height: 20.5px;
  }
  .contact-list li { display: flex; align-items: center; gap: 5px; white-space: nowrap; }
  .contact-list .icon { width: 13px; height: 13px; fill: var(--brand-blue); flex: none; }

  .info-band {
    position: absolute;
    left: 0; right: 0; bottom: 0;
    height: 88px;
    background: var(--brand-blue);
    color: #fff;
    text-align: center;
    font-size: 14px;
    line-height: 21px;
    padding-top: 18px;
  }
</style>
</head>
<body>

<section class="card card--front" aria-label="Business card front">
  <div class="wordmark">TraVorel</div>
  <p class="tagline">Connect<br>Collaborate<br>Achieve</p>

  <div class="name-band">
    <div class="person-name">DALE MERROW</div>
    <div class="person-title">Vice President</div>
  </div>

  <ul class="contact-list">
    <li>5870 Brookhollow Court</li>
    <li>Lindenvale, QX 908172</li>
    <li>
      <svg class="icon" viewBox="0 0 16 16" aria-hidden="true"><path d="M1 6c0-3 3-4 7-4s7 1 7 4l-3 1-1-2H5L4 7zM3 8h10l1 6H2z"/></svg>
      555-318-2046 x 100
    </li>
    <li>
      <svg class="icon" viewBox="0 0 16 16" aria-hidden="true"><path d="M1 6c0-3 3-4 7-4s7 1 7 4l-3 1-1-2H5L4 7zM3 8h10l1 6H2z"/></svg>
      555-318-2046 Toll Free
    </li>
    <li>
      <svg class="icon" viewBox="0 0 16 16" aria-hidden="true"><path d="M4 1h7v5H4zM2 7h12v7H2zM4 9v1h2V9zm4 0v1h2V9z"/></svg>
      555-742-9813
    </li>
    <li>
      <svg class="icon" viewBox="0 0 16 16" aria-hidden="true"><path d="M1 3h14v10H1zm1.5 1.5v.3L8 9l5.5-4.2v-.3zM2.5 6.6v5h11v-5L8 10.8z" fill-rule="evenodd"/></svg>
      name@travorel-example.net
    </li>
    <li>
      <svg class="icon" viewBox="0 0 16 16" aria-hidden="true"><path d="M8 1a7 7 0 1 0 0 14A7 7 0 0 0 8 1zm0 1.5c.8 0 1.7 1.6 2 4H6c.3-2.4 1.2-4 2-4zM2.6 7.5h2c0 .4 0 .7 0 1h-2zm8.8 0h2v1h-2zM6 9.5h4c-.3 2.4-1.2 4-2 4s-1.7-1.6-2-4z"/></svg>
      www.travorel-example.net
    </li>
  </ul>
</section>

<section class="card card--back" aria-label="Business card back">
  <div class="wordmark">TraVorel</div>
  <div class="info-band">
    <p>Established in 1998</p>
    <p>8(a)(w)(e), Cage #7KQW4, DUNS #412306957</p>
  </div>
</section>

</body>
</html>
```